Professional/Sleek card design for athletic apparel brand

Athletic apparel brand. Mainly focused on lifting weights/gym workouts. Logo and brand are already created. Must use brand logo and name. Creativity is welcome. Looking for a clean, modern, and sexy design.

```html
<!DOCTYPE html>
<html lang="en">
<head>
<meta charset="utf-8">
<title>Iron and Grit – Business Card</title>
<link href="https://fonts.googleapis.com/css2?family=Montserrat:wght@400;500;600;800&display=swap" rel="stylesheet">
<style>
  :root {
    --backdrop: #d7d7d7;
    --paper: #ffffff;
    --ink: #232323;
    --ink-soft: #3a3a3a;
    --card-dark: #222222;
    --pattern-light: #6e6e6e;
    --reverse-text: #ffffff;
  }
  html, body {
    margin: 0;
    padding: 0;
    width: 1200px;
    height: 1059px;
    overflow: hidden;
    background: var(--backdrop);
    font-family: "Montserrat", sans-serif;
  }
  .canvas {
    position: relative;
    width: 1200px;
    height: 1059px;
  }
  .card {
    position: absolute;
    left: 256px;
    width: 690px;
    border-radius: 20px;
    overflow: hidden;
  }
  /* Front */
  .card-front {
    top: 100px;
    height: 391px;
    background: var(--paper);
    color: var(--ink);
  }
  .wordmark {
    position: absolute;
    left: 37px;
    top: 42px;
    margin: 0;
    font-weight: 800;
    font-size: 34px;
    line-height: 1.05;
    letter-spacing: 0.5px;
    text-transform: uppercase;
    color: var(--ink);
  }
  .name-marker {
    position: absolute;
    left: 0;
    top: 200px;
    width: 19px;
    height: 39px;
    background: var(--ink);
  }
  .person {
    position: absolute;
    left: 37px;
    top: 196px;
  }
  .person-name {
    margin: 0;
    font-weight: 600;
    font-size: 21px;
    letter-spacing: 1px;
    text-transform: uppercase;
  }
  .person-title {
    margin: 2px 0 0;
    font-weight: 400;
    font-size: 15px;
    color: var(--ink-soft);
  }
  .contact-list {
    position: absolute;
    left: 35px;
    top: 277px;
    margin: 0;
    padding: 0;
    list-style: none;
  }
  .contact-list li {
    display: flex;
    align-items: center;
    gap: 7px;
    height: 28px;
    font-size: 15.5px;
    color: var(--ink-soft);
    letter-spacing: 0.3px;
  }
  .contact-list svg {
    width: 11px;
    height: 11px;
    fill: var(--ink);
  }
  .front-mark {
    position: absolute;
    right: 30px;
    top: 100px;
    width: 260px;
    text-align: center;
    font-weight: 800;
    font-size: 52px;
    line-height: 1.05;
    text-transform: uppercase;
    color: var(--ink);
  }
  /* Back */
  .card-back {
    top: 537px;
    height: 399px;
    background: var(--card-dark);
  }
  .back-pattern {
    position: absolute;
    inset: 0;
    background: linear-gradient(100deg, #1c1c1c 0%, #262626 45%, #3e3e3e 75%, var(--pattern-light) 100%);
  }
  .back-dot {
    position: absolute;
    left: 331px;
    top: 150px;
    width: 28px;
    height: 28px;
    border-radius: 50%;
    background: var(--reverse-text);
  }
  .back-wordmark {
    position: absolute;
    left: 0;
    right: 0;
    top: 226px;
    margin: 0;
    text-align: center;
    font-weight: 800;
    font-size: 16px;
    letter-spacing: 17px;
    text-transform: uppercase;
    color: var(--reverse-text);
  }
</style>
</head>
<body>
<main class="canvas">
  <section class="card card-front" aria-label="Card front">
    <h1 class="wordmark">Iron and<br>Grit</h1>
    <div class="name-marker"></div>
    <div class="person">
      <p class="person-name">Dean Halvorsen</p>
      <p class="person-title">CEO/Founder</p>
    </div>
    <ul class="contact-list">
      <li>
        <svg viewBox="0 0 24 24" aria-hidden="true"><path d="M6.6 10.8a15.1 15.1 0 0 0 6.6 6.6l2.2-2.2a1 1 0 0 1 1-.25 11.4 11.4 0 0 0 3.6.57 1 1 0 0 1 1 1V20a1 1 0 0 1-1 1A17 17 0 0 1 3 4a1 1 0 0 1 1-1h3.5a1 1 0 0 1 1 1c0 1.25.2 2.45.57 3.6a1 1 0 0 1-.25 1z"/></svg>
        (555) 014 2290
      </li>
      <li>
        <svg viewBox="0 0 24 24" aria-hidden="true"><path d="M2 5h20v14H2z M2 5l10 8 10-8" fill="none" stroke="#232323" stroke-width="0"/><path d="M2 6.5 12 13l10-6.5V19H2z"/><path d="M2 5h20l-10 6.5z"/></svg>
        hello@ironandgrit.com
      </li>
      <li>
        <svg viewBox="0 0 24 24" aria-hidden="true"><circle cx="12" cy="12" r="9.5" fill="none" stroke="#232323" stroke-width="2"/><ellipse cx="12" cy="12" rx="4" ry="9.5" fill="none" stroke="#232323" stroke-width="2"/><path d="M2.5 12h19M4 7h16M4 17h16" stroke="#232323" stroke-width="1.6"/></svg>
        www.ironandgrit.com
      </li>
    </ul>
    <div class="front-mark">Iron<br>and<br>Grit</div>
  </section>

  <section class="card card-back" aria-label="Card back">
    <div class="back-pattern" role="img" aria-label="Repeating brand pattern fading from black to grey across the card"></div>
    <div class="back-dot"></div>
    <p class="back-wordmark">Iron and Grit</p>
  </section>
</main>
</body>
</html>
```